Taomeng business card -we import and distributed Chinese herbal medicine into Australia for prac...

We need a business card for our recently purchased and rebranded company. We are a small family run business - husband and wife team. Our logo is red and black, and we would like the card to be white, with an element of gold in the design (the first cloud in the attached png) which when printed we would like embossed in gold. Our website uses Chinese water colour paintings in the banners (www.taomeng.net.au) so a design that is in harmony with this would be ideal.
side one needs to include:

Target Market(s)

potential customers

Industry/Entity Type

Health And Wellness

Contact Information for Business Card

Side 1
logo,
Edmund Varsk Director
Practitioner Support and Education
0491 722 413
edmund@taomeng.net.au
218 Colbury St, Kelmarra, WA, 6088

side 2 needs to include:
logo
Priscilla Moult Director
Orders, Accounts and Despatch
0487 530 619
priscilla@taomeng.net.au

Font styles to use
Serif

Colors

Designer to choose colors to be used in the design.

Requirements
Must have
• black, red, gold colours
Nice to have
• we like the font papyrus (mac font)

```html
<!DOCTYPE html>
<html lang="en">
<head>
<meta charset="utf-8">
<title>Taomeng business cards</title>
<link rel="stylesheet" href="https://fonts.googleapis.com/css2?family=Tinos:wght@400;700&display=swap">
<style>
  :root {
    --backdrop: #e9e6e1;
    --card: #f2f4f6;
    --ink: #1e2540;
    --red: #e0401f;
    --seal: #d8371c;
    --wash-deep: #2f5f93;
    --wash-mid: #6f97c0;
    --wash-pale: #c9d8e6;
    --icon-bg: #e24a2a;
  }
  * { box-sizing: border-box; margin: 0; padding: 0; }
  html, body { width: 900px; height: 1200px; overflow: hidden; }
  body {
    background: var(--backdrop);
    position: relative;
    font-family: "Tinos", "Times New Roman", serif;
    color: var(--ink);
  }
  .card {
    position: absolute;
    left: 80px;
    width: 735px;
    height: 430px;
    border-radius: 22px;
    overflow: hidden;
    background: linear-gradient(180deg, #f6f7f9 0%, var(--card) 60%, #e8eef4 100%);
    box-shadow: 0 6px 18px rgba(0,0,0,0.18);
  }
  .card--front { top: 128px; }
  .card--back { top: 645px; }
  .art { position: absolute; display: block; }

  .mountain-band {
    left: 0; right: 0; bottom: 0;
    height: 100px;
    background: linear-gradient(180deg, rgba(201,216,230,0) 0%, var(--wash-pale) 25%, var(--wash-mid) 55%, var(--wash-deep) 85%, #24507f 100%);
  }
  .far-hills {
    background: radial-gradient(ellipse at 50% 100%, rgba(174,196,218,0.75) 0%, rgba(200,215,230,0.35) 55%, rgba(242,244,246,0) 75%);
  }
  .moon {
    left: 455px; top: 22px;
    width: 232px; height: 232px;
    border-radius: 50%;
    background: radial-gradient(circle at 40% 30%, #3f6e9e 0%, #5f88b2 45%, #9db8d2 80%, #c6d6e5 100%);
  }
  .trees {
    left: 0; top: 0;
    width: 220px; height: 360px;
    background: radial-gradient(ellipse at 30% 35%, rgba(63,100,145,0.55) 0%, rgba(120,150,185,0.3) 45%, rgba(242,244,246,0) 72%);
  }
  .cloud {
    left: 232px; top: 52px;
    width: 146px; height: 66px;
    border-radius: 30px;
    background: linear-gradient(90deg, #7ea6cc, #9dbedb);
    opacity: 0.85;
  }

  .brand {
    position: absolute;
    display: flex;
    align-items: center;
    gap: 18px;
  }
  .brand__mark {
    width: 56px; height: 56px;
    background: var(--seal);
    flex: none;
  }
  .brand__name {
    font-size: 60px;
    font-weight: 400;
    letter-spacing: 2px;
    color: var(--ink);
    line-height: 64px;
  }
  .brand__line { display: block; }
  .card--front .brand { left: 45px; top: 66px; }
  .card--back .brand { left: 110px; top: 140px; }

  .person { position: absolute; }
  .person__name {
    font-size: 22px;
    font-weight: 700;
    letter-spacing: 0.5px;
    color: var(--ink);
    text-transform: uppercase;
    line-height: 1.1;
  }
  .person__role {
    font-size: 16px;
    color: var(--red);
    line-height: 23px;
  }
  .card--front .person { left: 45px; top: 264px; }
  .card--front .person__name { margin-bottom: 5px; }
  .card--back .person { right: 46px; top: 58px; text-align: right; }
  .card--back .person__name { margin-bottom: 4px; }

  .contacts {
    position: absolute;
    list-style: none;
    font-size: 16px;
    line-height: 24px;
    color: var(--ink);
  }
  .contacts li { display: flex; align-items: center; gap: 7px; white-space: nowrap; }
  .card--front .contacts { left: 378px; top: 262px; }
  .card--back .contacts { right: 46px; top: 243px; }
  .card--back .contacts li { justify-content: flex-end; }
  .icon {
    width: 18px; height: 18px;
    border-radius: 3px;
    background: var(--icon-bg);
    flex: none;
  }
  .icon svg { display: block; width: 18px; height: 18px; }
</style>
</head>
<body>

  <section class="card card--front" aria-label="Front card">
    <div class="art far-hills" style="left:380px; bottom:60px; width:360px; height:120px;" role="img" aria-label="Faint watercolour hills in the distance"></div>
    <div class="art moon" role="img" aria-label="Ink-wash moon with flying cranes"></div>
    <div class="art mountain-band" role="img" aria-label="Blue watercolour mountain range along the bottom edge"></div>

    <div class="brand">
      <span class="brand__mark"></span>
      <span class="brand__name"><span class="brand__line">TAO</span><span class="brand__line">MENG</span></span>
    </div>

    <div class="person">
      <h1 class="person__name">Edmund Varsk</h1>
      <p class="person__role">Director</p>
      <p class="person__role">Practitioner Support and Education</p>
    </div>

    <ul class="contacts">
      <li><span class="icon"><svg viewBox="0 0 18 18"><path d="M5.5 4l2 2.3-1 1.4c.8 1.6 2 2.9 3.6 3.7l1.4-1 2.3 2-1 1.6c-4.5-.4-8.3-4.3-8.7-8.7z" fill="#fff"/></svg></span>0491 722 413</li>
      <li><span class="icon"><svg viewBox="0 0 18 18"><rect x="4" y="5.5" width="10" height="7" fill="none" stroke="#fff" stroke-width="1.3"/><path d="M4 5.5l5 4 5-4" fill="none" stroke="#fff" stroke-width="1.3"/></svg></span>edmund@taomeng.net.au</li>
      <li><span class="icon"><svg viewBox="0 0 18 18"><path d="M9 3.5a3.8 3.8 0 0 1 3.8 3.8c0 2.8-3.8 7.2-3.8 7.2S5.2 10.1 5.2 7.3A3.8 3.8 0 0 1 9 3.5z" fill="#fff"/><circle cx="9" cy="7.3" r="1.4" fill="#e24a2a"/></svg></span>218 Colbury St, Kelmarra, WA, 6088</li>
    </ul>
  </section>

  <section class="card card--back" aria-label="Back card">
    <div class="art far-hills" style="left:330px; top:140px; width:330px; height:150px;" role="img" aria-label="Faint watercolour mountain peaks"></div>
    <div class="art trees" role="img" aria-label="Ink-painted bare trees on the left edge"></div>
    <div class="art cloud" role="img" aria-label="Stylised cloud ornament"></div>
    <div class="art mountain-band" role="img" aria-label="Blue watercolour mountain range along the bottom edge"></div>

    <div class="person">
      <h1 class="person__name">Priscilla Moult</h1>
      <p class="person__role">Director</p>
      <p class="person__role">Orders, Accounts and Despatch</p>
    </div>

    <div class="brand">
      <span class="brand__mark"></span>
      <span class="brand__name"><span class="brand__line">TAO</span><span class="brand__line">MENG</span></span>
    </div>

    <ul class="contacts">
      <li>0487 530 619<span class="icon"><svg viewBox="0 0 18 18"><path d="M5.5 4l2 2.3-1 1.4c.8 1.6 2 2.9 3.6 3.7l1.4-1 2.3 2-1 1.6c-4.5-.4-8.3-4.3-8.7-8.7z" fill="#fff"/></svg></span></li>
      <li>priscilla@taomeng.net.au<span class="icon"><svg viewBox="0 0 18 18"><rect x="4" y="5.5" width="10" height="7" fill="none" stroke="#fff" stroke-width="1.3"/><path d="M4 5.5l5 4 5-4" fill="none" stroke="#fff" stroke-width="1.3"/></svg></span></li>
      <li>218 Colbury St, Kelmarra, WA, 6088<span class="icon"><svg viewBox="0 0 18 18"><path d="M9 3.5a3.8 3.8 0 0 1 3.8 3.8c0 2.8-3.8 7.2-3.8 7.2S5.2 10.1 5.2 7.3A3.8 3.8 0 0 1 9 3.5z" fill="#fff"/><circle cx="9" cy="7.3" r="1.4" fill="#e24a2a"/></svg></span></li>
    </ul>
  </section>

</body>
</html>
```